Marigold Cleaning Service LTD its all about cleaning ( Domestic Cleaning, Commercial Cleaning, Student Accommodations, Corridors, Halls & Common Areas). I'm looking for POSH/ ELEGANT LOOKING design of flyers, which presents all Services we provide, it also should include 5% discount for new customers, contact details: website: www.marigold-clean.example.co.uk email address: marigoldservice@mailbox-example.com Mobile phone no: 07700900417 and home no: 01632960582 . I would like to include logo of the company, without any pictures of buckets etc.(that in my opinion pictures like that looks "cheap"). It should be design which perfectly match logo of the company, I would like also to include slogan of Marigold "You Deserve Marigold Cleaners". I was thinking to make those flyers, bright "clean" (maybe background could be beige color, on the other hand I think Navy color looks elegant as well, I'm looking for something posh NOT like some random cleaning company, It should be something UNIQUE). Of course by this flyers Marigold Cleaning Service should increase profits. If you will have any draft or any questions please contact me at any time on email: h.walters@mailbox-example.com or by phone: 07700900417
Best Regards
Hilda Walters
Marigold Cleaning Service LTD

```html
<!DOCTYPE html>
<html lang="en">
<head>
<meta charset="utf-8">
<title>Marigold Cleaning Service LTD – Flyer</title>
<link rel="stylesheet" href="https://fonts.googleapis.com/css2?family=Oswald:wght@400;500;600&family=Pathway+Gothic+One&family=Playfair+Display+SC:wght@400;900&family=Arimo&display=swap">
<style>
  :root {
    --navy: #1d2a4b;
    --navy-deep: #141e38;
    --navy-ink: #1f2d52;
    --beige: #bab3a5;
    --beige-light: #c9c2b4;
    --beige-text: #a8a294;
    --rule: #c8c1b3;
    --logo-text: #b9b7c2;
  }
  * { margin: 0; padding: 0; box-sizing: border-box; }
  html, body { width: 1200px; height: 900px; overflow: hidden; background: var(--navy-deep); }
  .flyer {
    position: relative; width: 1200px; height: 900px; overflow: hidden;
    background: radial-gradient(ellipse at 50% 45%, var(--navy) 40%, var(--navy-deep) 100%);
  }
  .fold { position: absolute; left: 598px; top: 0; width: 3px; height: 900px; background: var(--rule); opacity: .85; }
  .rule { position: absolute; height: 2px; background: var(--rule); }
  .rule--dark { background: var(--navy-ink); height: 2px; }

  /* Front panel */
  .brand {
    position: absolute; left: 130px; top: 92px; width: 320px;
    display: flex; align-items: center; gap: 12px;
    font-family: "Arimo", sans-serif; font-weight: 400; color: var(--logo-text);
  }
  .brand__mark { width: 20px; height: 20px; border-radius: 50%; background: var(--logo-text); flex: none; }
  .brand__name { font-size: 32px; line-height: 1.3; text-align: center; }
  .brand__name small { display: block; font-size: 22px; margin-top: 10px; }

  .offer {
    position: absolute; left: 20px; top: 218px; width: 558px; height: 454px;
    background: radial-gradient(ellipse at 50% 50%, var(--beige-light), var(--beige) 80%);
  }
  .offer__presents {
    position: absolute; top: 40px; width: 100%; text-align: center;
    font-family: "Playfair Display SC", serif; font-size: 19px; color: var(--navy-ink);
  }
  .offer__splash {
    position: absolute; left: 12px; top: 92px; width: 532px; height: 320px;
    border-radius: 40px 60px 20px 20px;
    background: linear-gradient(180deg, var(--navy-ink) 0%, var(--navy-ink) 55%, rgba(31,45,82,.35) 100%);
  }
  .offer__headline {
    position: absolute; top: 130px; width: 100%; text-align: center;
    font-family: "Playfair Display SC", serif; font-weight: 900; font-size: 34px;
    color: var(--beige-light); text-shadow: 2px 2px 2px #000;
  }
  .offer__for {
    position: absolute; top: 183px; left: 92px; width: 340px;
    display: flex; align-items: center; gap: 10px;
    font-family: "Oswald", sans-serif; font-size: 19px; color: var(--beige-light);
  }
  .offer__for::before, .offer__for::after { content: ""; flex: 1; height: 2px; background: var(--beige-light); }
  .offer__audience {
    position: absolute; top: 222px; width: 100%; text-align: center;
    font-family: "Oswald", sans-serif; font-weight: 500; font-size: 36px;
    color: var(--beige-light); text-shadow: 2px 2px 2px #000;
  }

  .slogan { position: absolute; left: 0; top: 742px; width: 598px; text-align: center; color: var(--beige-text); text-shadow: 2px 3px 3px #000; white-space: nowrap; }
  .slogan__lead { font-family: "Oswald", sans-serif; font-size: 36px; letter-spacing: 24px; line-height: 1; padding-left: 24px; }
  .slogan__name { display: inline-block; font-family: "Oswald", sans-serif; font-weight: 600; font-size: 58px; line-height: 1.1; transform: scale(.84, 1.1); transform-origin: center top; margin-top: 2px; }

  /* Back panel */
  .card {
    position: absolute; left: 620px; width: 560px;
    background: radial-gradient(ellipse at 50% 50%, var(--beige-light), var(--beige) 85%);
    color: var(--navy-ink);
  }
  .services { top: 28px; height: 312px; }
  .services__title {
    position: absolute; top: 24px; width: 100%; text-align: center; white-space: nowrap;
    font-family: "Pathway Gothic One", sans-serif; font-variant: small-caps; font-weight: 400;
    font-size: 56px; line-height: 1.1; letter-spacing: 2px;
    -webkit-text-stroke: 1px var(--navy-ink);
  }
  .services__list { position: absolute; left: 75px; top: 100px; list-style: none; }
  .services__list li {
    font-family: "Pathway Gothic One", sans-serif; font-size: 31px; line-height: 35px;
    display: flex; align-items: center; gap: 12px;
  }
  .services__list svg { width: 13px; height: 16px; }

  .sweeper {
    position: absolute; left: 620px; top: 378px; width: 540px; height: 184px;
    background: linear-gradient(90deg, rgba(29,42,75,0) 0%, rgba(200,193,179,.18) 60%, rgba(200,193,179,.35) 100%);
    border-bottom: 6px solid rgba(200,193,179,.55);
  }

  .contact { top: 592px; height: 238px; text-align: center; }
  .contact__title { margin-top: 28px; font-family: "Oswald", sans-serif; font-weight: 500; font-size: 34px; line-height: 1.2; }
  .contact__list { list-style: none; margin-top: 6px; font-family: "Oswald", sans-serif; font-weight: 500; font-size: 19px; line-height: 35px; }
</style>
</head>
<body>
<main class="flyer">
  <section class="front">
    <div class="brand">
      <span class="brand__mark"></span>
      <p class="brand__name">Marigold<small>Cleaning Service LTD</small></p>
    </div>
    <div class="rule" style="left:12px; top:209px; width:574px;"></div>

    <div class="offer">
      <p class="offer__presents">Presents...</p>
      <div class="offer__splash" role="img" aria-label="Navy paint splash with drips and a paint brush stroke"></div>
      <p class="offer__headline">5% Discount</p>
      <p class="offer__for">FOR</p>
      <p class="offer__audience">NEW CUSTOMERS</p>
    </div>
    <div class="rule" style="left:12px; top:684px; width:574px;"></div>

    <div class="slogan">
      <p class="slogan__lead">YOU DESERVE</p>
      <p class="slogan__name">MARIGOLD CLEANERS</p>
    </div>
  </section>

  <div class="fold"></div>

  <section class="back">
    <div class="card services">
      <div class="rule rule--dark" style="left:12px; top:10px; width:536px;"></div>
      <h2 class="services__title">You Name it we Clean it!</h2>
      <ul class="services__list">
        <li><svg viewBox="0 0 13 16"><path d="M1 0 L13 8 L1 16 L5 8 Z" fill="currentColor"/></svg>DOMESTIC CLEANING</li>
        <li><svg viewBox="0 0 13 16"><path d="M1 0 L13 8 L1 16 L5 8 Z" fill="currentColor"/></svg>COMMERCIAL CLEANING</li>
        <li><svg viewBox="0 0 13 16"><path d="M1 0 L13 8 L1 16 L5 8 Z" fill="currentColor"/></svg>STUDENT ACCOMMODATIONS</li>
        <li><svg viewBox="0 0 13 16"><path d="M1 0 L13 8 L1 16 L5 8 Z" fill="currentColor"/></svg>CORRIDORS</li>
        <li><svg viewBox="0 0 13 16"><path d="M1 0 L13 8 L1 16 L5 8 Z" fill="currentColor"/></svg>HALLS AND COMMON AREAS</li>
      </ul>
      <div class="rule rule--dark" style="left:12px; top:295px; width:536px;"></div>
    </div>

    <div class="sweeper" role="img" aria-label="Sketched silhouette of a child sweeping a clean stroke across the floor with a broom"></div>

    <div class="card contact">
      <div class="rule rule--dark" style="left:12px; top:12px; width:536px;"></div>
      <h2 class="contact__title">CONTACT US</h2>
      <ul class="contact__list">
        <li>WEBSITE: WWW.MARIGOLD-CLEAN.EXAMPLE.CO.UK</li>
        <li>EMAIL ADDRESS: MARIGOLDSERVICE@MAILBOX-EXAMPLE.COM</li>
        <li>MOBILE : 07700900417</li>
        <li>HOME : 01632960582</li>
      </ul>
      <div class="rule rule--dark" style="left:12px; top:222px; width:536px;"></div>
    </div>
  </section>
</main>
</body>
</html>
```